Website Navigation Redesign

We are looking for a redesign of the navigation system of our website. We prefer a clean, simple, modern look.
We are looking for three elements:
1. A top level navigation that jumps between 4 subdomains: Wealth Management, Direct Indexing, Ethical Investing and Superannuation
2. A secondary navigation for each subdomain similar to the one on this page: https://parcelvault.au/ . The elements will be (a) 3-5 menu items (b) the ability to have submenus (c) a logo (d) a login button (e) a "call-to-action" button
3. A standard footer. See the footer from https://tarnbrookfund.com/ for the content to be included in the footer.
Each of the sub domains have very similar logos that we also want displayed (see uploaded image)
We are looking for 1 web page version and 1 mobile version.
It will be hosted on Hubspot CMS, and so solutions that will fit easily into that solution without custom coding will be preferred.
Our typical fonts are Ubuntu and Roboto. We prefer solutions using those fonts
Thanks
Target Market(s)
Small investors
Industry/Entity Type
Financial Services
Coding
Coded - Design and coding required
Number of Pages Required
1 page

```html
<!DOCTYPE html>
<html lang="en">
<head>
<meta charset="utf-8">
<title>Tarnbrook Wealth – Mobile Navigation</title>
<link href="https://fonts.googleapis.com/css2?family=Roboto:wght@400;500&family=Ubuntu:wght@500;700&display=swap" rel="stylesheet">
<style>
  :root {
    --brand-blue: #1a5aab;
    --brand-navy: #0e3f86;
    --ink: #1c1c1c;
    --white: #ffffff;
    --mist: #e9eef3;
    --skyline-light: #bfd3df;
    --skyline-deep: #6f9db4;
  }
  html, body {
    margin: 0;
    padding: 0;
    overflow: hidden;
  }
  body {
    width: 1191px;
    height: 1200px;
    position: relative;
    background: var(--white);
    font-family: "Roboto", Arial, sans-serif;
  }
  .skyline {
    position: absolute;
    left: 0;
    top: 520px;
    width: 1191px;
    height: 680px;
    background:
      radial-gradient(ellipse at 70% 85%, var(--skyline-deep) 0%, rgba(111,157,180,0.55) 30%, rgba(233,238,243,0) 65%),
      linear-gradient(180deg, rgba(255,255,255,1) 0%, var(--mist) 40%, var(--skyline-light) 100%);
  }
  .subdomain-bar {
    position: absolute;
    left: 0;
    top: 0;
    width: 1191px;
    height: 150px;
  }
  .subdomain-bar svg { position: absolute; left: 0; top: 0; }
  .subdomain-links {
    position: absolute;
    top: 30px;
    left: 0;
    margin: 0;
    padding: 0;
    list-style: none;
  }
  .subdomain-links li {
    position: absolute;
    white-space: nowrap;
    color: var(--white);
    font-weight: 500;
    font-size: 29px;
    line-height: 36px;
  }
  .brand {
    position: absolute;
    left: 43px;
    top: 245px;
    width: 374px;
    height: 302px;
    background: var(--white);
    display: flex;
    flex-direction: column;
    justify-content: center;
    padding-left: 30px;
    box-sizing: border-box;
    font-family: "Ubuntu", Arial, sans-serif;
    font-weight: 700;
    color: var(--brand-navy);
    font-size: 62px;
    line-height: 1.05;
  }
  .header-actions {
    position: absolute;
    top: 331px;
    left: 705px;
  }
  .action {
    position: absolute;
    width: 120px;
    height: 120px;
    border-radius: 50%;
    box-sizing: border-box;
    border: 6px solid var(--brand-navy);
    background: var(--white);
    display: flex;
    align-items: center;
    justify-content: center;
  }
  .action--menu { left: 0; background: var(--brand-navy); border-color: var(--brand-navy); }
  .action--login { left: 144px; }
  .action--cta { left: 285px; }
  .menu-indicator {
    position: absolute;
    left: 644px;
    top: 444px;
  }
  .menu-dropdown {
    position: absolute;
    left: 564px;
    top: 452px;
    width: 296px;
    height: 477px;
    background: var(--white);
    box-shadow: 0 4px 18px rgba(0,0,0,0.12);
    margin: 0;
    padding: 60px 0 0 57px;
    box-sizing: border-box;
    list-style: none;
  }
  .menu-dropdown li {
    font-size: 35px;
    line-height: 75px;
    color: var(--ink);
    margin-top: -20px;
    height: 75px;
  }
  .menu-dropdown li:first-child { margin-top: 0; }
</style>
</head>
<body>
  <div class="skyline" role="img" aria-label="City skyline with rising stock chart candles"></div>

  <nav class="subdomain-bar" aria-label="Subdomains">
    <svg width="1191" height="150" viewBox="0 0 1191 150">
      <path d="M0 0 H1191 V92 C900 128 300 128 0 92 Z" fill="var(--brand-blue)"/>
      <path d="M0 96 C300 132 900 132 1191 96" fill="none" stroke="var(--white)" stroke-width="4"/>
      <path d="M0 104 C300 140 900 140 1191 104" fill="none" stroke="var(--brand-navy)" stroke-width="6"/>
      <circle cx="909" cy="121" r="11" fill="var(--brand-navy)"/>
    </svg>
    <ul class="subdomain-links">
      <li style="left:52px">Direct Indexing</li>
      <li style="left:311px">Superannuation</li>
      <li style="left:572px">Ethical Investing</li>
      <li style="left:837px">Wealth Management</li>
    </ul>
  </nav>

  <div class="brand"><span>Tarnbrook</span><span>Wealth</span></div>

  <div class="header-actions">
    <div class="action action--menu" aria-label="Menu">
      <svg width="54" height="46" viewBox="0 0 54 46">
        <rect x="0" y="0" width="54" height="9" rx="4.5" fill="#fff"/>
        <rect x="0" y="18.5" width="54" height="9" rx="4.5" fill="#fff"/>
        <rect x="0" y="37" width="54" height="9" rx="4.5" fill="#fff"/>
      </svg>
    </div>
    <div class="action action--login" aria-label="Log in">
      <svg width="52" height="56" viewBox="0 0 52 56">
        <circle cx="26" cy="14" r="13" fill="var(--brand-navy)"/>
        <path d="M2 56 V46 C2 36 10 31 18 31 H34 C42 31 50 36 50 46 V56 Z" fill="var(--brand-navy)"/>
      </svg>
    </div>
    <div class="action action--cta" aria-label="Get started">
      <svg width="56" height="56" viewBox="0 0 56 56">
        <path d="M4 52 L8 36 L38 6 L50 18 L20 48 Z" fill="var(--brand-navy)"/>
        <path d="M41 3 L44 0 L56 12 L53 15 Z" fill="var(--brand-navy)"/>
      </svg>
    </div>
  </div>

  <svg class="menu-indicator" width="134" height="26" viewBox="0 0 134 26">
    <rect x="0" y="10" width="134" height="6" fill="var(--brand-navy)"/>
    <rect x="59" y="5" width="16" height="16" transform="rotate(45 67 13)" fill="var(--brand-navy)"/>
  </svg>

  <ul class="menu-dropdown">
    <li>Home</li>
    <li>Investments</li>
    <li>Blog</li>
    <li>About Us</li>
    <li>Contact Us</li>
  </ul>
</body>
</html>
```